hfdhddfgfhfghfghgfhfhfhgfhfhfh

Industry/Entity Type

Painting

Logo Text

KOLBEC Painting

Logo styles of interest
Wordmark Logo
Requirements
Should not have
• Paintbrushes or rollers etc....

```html
<!DOCTYPE html>
<html lang="en">
<head>
<meta charset="utf-8">
<title>Kolbec Painting — Stationery</title>
<link rel="stylesheet" href="https://fonts.googleapis.com/css2?family=Inter:ital,wght@0,400;0,600;0,700;1,400&display=swap">
<style>
  :root {
    --backdrop: #f3f3f3;
    --paper: #ececec;
    --card-light: #ededed;
    --brand-blue: #0096db;
    --ink: #1b1b1b;
    --ink-soft: #333333;
    --white: #ffffff;
    --font-text: "Inter", "Helvetica Neue", Arial, sans-serif;
  }
  * { margin: 0; padding: 0; box-sizing: border-box; }
  html, body {
    width: 1200px;
    height: 1000px;
    overflow: hidden;
    background: var(--backdrop);
    font-family: var(--font-text);
    color: var(--ink);
  }
  .canvas { position: relative; width: 1200px; height: 1000px; }

  .letterhead {
    position: absolute;
    left: 135px; top: 190px;
    width: 458px; height: 620px;
    background: var(--paper);
  }
  .letterhead__wordmark {
    position: absolute;
    left: 0; right: 0; top: 20px;
    text-align: center;
    font-size: 11px;
    font-weight: 600;
    letter-spacing: -0.2px;
    color: var(--ink);
  }

  .card {
    position: absolute;
    width: 421px; height: 240px;
  }
  .card--front {
    left: 645px; top: 297px;
    background: var(--card-light);
  }
  .card--back {
    left: 644px; top: 570px;
    background: var(--brand-blue);
    display: flex;
    flex-direction: column;
    align-items: center;
    justify-content: center;
  }

  .card__wordmark {
    position: absolute;
    left: 21px; top: 30px;
    font-size: 30px;
    font-weight: 600;
    letter-spacing: -0.8px;
    color: var(--ink);
  }

  .contact {
    position: absolute;
    left: 234px; top: 103px;
    font-size: 12.5px;
    line-height: 1.35;
    color: var(--ink);
  }
  .contact__name { font-weight: 600; font-size: 13px; }
  .contact__role { font-style: italic; font-size: 11px; color: var(--ink-soft); }
  .contact__lines { margin-top: 24px; }
  .contact__abn { margin-top: 10px; }
  .contact__abn-label { font-weight: 700; font-size: 11px; }

  .card__wordmark--large {
    font-size: 40px;
    font-weight: 600;
    letter-spacing: -1px;
    color: var(--white);
    line-height: 1;
    margin-top: 6px;
  }
  .card__tagline {
    margin-top: 6px;
    font-size: 8.5px;
    font-weight: 700;
    letter-spacing: 1.1px;
    color: var(--ink);
  }
</style>
</head>
<body>
  <main class="canvas">
    <section class="letterhead">
      <div class="letterhead__wordmark">Kolbec Painting</div>
    </section>

    <section class="card card--front">
      <div class="card__wordmark">Kolbec Painting</div>
      <div class="contact">
        <div class="contact__name">Lukas Kolbec</div>
        <div class="contact__role">Managing Director</div>
        <div class="contact__lines">
          <div>041-555-0193</div>
          <div>kolbecpainting@mailbox.com</div>
        </div>
        <div class="contact__abn"><span class="contact__abn-label">ABN:</span> 31 602 557 190</div>
      </div>
    </section>

    <section class="card card--back">
      <div class="card__wordmark--large">Kolbec Painting</div>
      <div class="card__tagline">DOMESTIC, RESIDENTIAL &amp; COMMERCIAL</div>
    </section>
  </main>
</body>
</html>
```